LABEL DESIGNS FOR SKINCARE LINE

Hello we are needing 12 label various label designs but would like to see you design ONE. We will pick winner from this and send the rest.
LABEL SIZE -2x7
JAR SIZE IS - 8oz
LOGOS FILES BELOW
https://files.pavorna-share.net/drive/folders/7xk3q-wumTrazPLoqVnnRTZBKHAE2DpLW
INFORMATION FOR LABEL
Calm Dune Hush Whipped Body Sugar Scrub 8oz
Ideal for all Skin Types
Ingredients:
Pure Cane Sugar, Extra Virgin Coconut Oil, Mango Butter, Kukum Butter, Emulsifying Wax, Jojoba Seed Oil, Sweet Almond Oil, Strawberry Essential Oil, and Pomegranate Essential Oil.
Directions to use Body Sugar Scrub:
Apply to wet skin gently in a circular motion on desired body area, hands, feet, legs, arms, etc. Once you have a good scrub, rinse, pat dry, and enjoy soft, hydrated skin. Best to use in the shower. Use between 2-3 times a week if needed.
*Cautions:
(1) Allergy: Approach this product with extreme caution, if you have allergies
(2) Avoid direct contact with eyes
Storage/Shelf Life of Product:
For best results, stir/mix scrub with the wooden or plastic spoon before each use. The shelf life of all sugar scrubs is 6-8 weeks. Keep the product in a cool, dry place, away from hot or heated temperatures.
All Natural, Cruelty-Free, Vegan Free
No Mineral Oil
No Petroleum
No Parabens

```html
<!DOCTYPE html>
<html lang="en">
<head>
<meta charset="utf-8">
<title>Calm Dune Hush – Whipped Body Sugar Scrub Labels</title>
<link rel="stylesheet" href="https://fonts.googleapis.com/css2?family=Oswald:wght@300;500;700&family=Playfair+Display:wght@700;900&family=Pacifico&family=Lobster&display=swap">
<style>
  :root {
    --canvas: #ffffff;
    --red-deep: #d8141f;
    --red-mid: #ee2a33;
    --red-light: #f65a5e;
    --pink-hot: #ea2a78;
    --pink-soft: #f25a9a;
    --pink-red: #f0303e;
    --ink: #ffffff;
  }
  html, body {
    margin: 0;
    padding: 0;
    width: 864px;
    height: 1200px;
    overflow: hidden;
    background: var(--canvas);
  }
  .sheet {
    position: relative;
    width: 864px;
    height: 1200px;
  }
  .label {
    position: absolute;
    left: 86px;
    width: 694px;
    height: 198px;
    overflow: hidden;
    color: var(--ink);
    font-family: "Oswald", sans-serif;
  }
  .label--glitter { top: 652px; }
  .label--candy { top: 930px; }

  .label__bg {
    position: absolute;
    inset: 0;
  }
  .label--glitter .label__bg {
    background:
      radial-gradient(ellipse at 70% 60%, rgba(255,160,160,.35), transparent 55%),
      radial-gradient(ellipse at 30% 20%, rgba(255,120,120,.25), transparent 50%),
      linear-gradient(180deg, var(--red-mid), var(--red-deep));
  }
  .label--candy .label__bg {
    background:
      linear-gradient(115deg, var(--pink-red) 0%, var(--pink-hot) 30%, var(--pink-soft) 48%, var(--pink-hot) 62%, var(--pink-red) 100%);
  }

  .column {
    position: absolute;
    top: 24px;
    font-weight: 300;
    font-size: 9.6px;
    line-height: 13.2px;
  }
  .column p { margin: 0 0 12px; }
  .column strong { font-weight: 700; }
  .column--left { left: 28px; width: 184px; }
  .column--right { left: 484px; width: 184px; }

  .claims {
    margin-top: 4px;
    text-align: center;
    font-weight: 700;
    font-size: 9.2px;
    line-height: 12.4px;
  }

  .front {
    position: absolute;
    left: 262px;
    top: 12px;
    width: 180px;
    text-align: center;
  }
  .brand {
    font-family: "Playfair Display", serif;
    font-weight: 700;
    font-size: 16px;
    letter-spacing: -0.2px;
    margin: 0;
  }
  .product-kicker {
    font-family: "Lobster", cursive;
    font-size: 22px;
    line-height: 1;
    margin: 12px 0 0;
  }
  .product-main {
    margin: 0;
    line-height: 1;
  }
  .label--glitter .product-main {
    font-family: "Playfair Display", serif;
    font-weight: 900;
    font-size: 52px;
    margin-top: -2px;
  }
  .label--candy .product-kicker { font-size: 18px; margin-top: 10px; }
  .label--candy .product-main {
    font-family: "Pacifico", cursive;
    font-size: 46px;
    margin-top: -6px;
    line-height: 1.05;
  }
  .product-type {
    font-weight: 500;
    font-size: 14.5px;
    margin: 4px 0 0;
  }
  .label--candy .product-type { margin-top: 0; }
  .size {
    font-weight: 500;
    font-size: 14.5px;
    margin: 6px 0 0;
  }
</style>
</head>
<body>
<main class="sheet">

  <section class="label label--glitter">
    <div class="label__bg" role="img" aria-label="Red sparkling glitter background texture"></div>
    <div class="column column--left">
      <p><strong>Ingredients:</strong> Pure Cane Sugar, Extra Virgin Coconut Oil, Mango Butter, Kukum Butter, Emulsifying Wax, Jojoba Seed Oil, Sweet Almond Oil, Strawberry Essential Oil, and Pomegranate Essential Oil.</p>
      <p><strong>Storage/Shelf Life of Product:</strong> For best results, stir/mix scrub with the wooden or plastic spoon before each use. The shelf life of all sugar scrubs is 6-8 weeks. Keep the product in a cool, dry place, away from hot or heated temperatures.</p>
    </div>
    <div class="front">
      <p class="brand">Sugar Lane</p>
      <p class="product-kicker">Calm Dune</p>
      <p class="product-main">Hush</p>
      <p class="product-type">Whipped Body Sugar Scrub</p>
      <p class="size">8oz</p>
    </div>
    <div class="column column--right">
      <p><strong>Directions:</strong> Apply to wet skin gently in a circular motion on desired body area, hands, feet, legs, arms, etc. Once you have a good scrub, rinse, pat dry, and enjoy soft, hydrated skin. Best to use in the shower. Use between 2-3 times a week if needed.</p>
      <p><strong>Cautions:</strong> (1) Allergy: Approach this product with extreme caution, if you have allergies (2) Avoid direct contact with eyes</p>
      <div class="claims">All Natural, Cruelty-Free, Vegan Free<br>No Mineral Oil | No Petroleum | No Parabens</div>
    </div>
  </section>

  <section class="label label--candy">
    <div class="label__bg" role="img" aria-label="Pink and red diagonal candy bands with faint sparkle pattern"></div>
    <div class="column column--left">
      <p><strong>Ingredients:</strong> Pure Cane Sugar, Extra Virgin Coconut Oil, Mango Butter, Kukum Butter, Emulsifying Wax, Jojoba Seed Oil, Sweet Almond Oil, Strawberry Essential Oil, and Pomegranate Essential Oil.</p>
      <p><strong>Storage/Shelf Life of Product:</strong> For best results, stir/mix scrub with the wooden or plastic spoon before each use. The shelf life of all sugar scrubs is 6-8 weeks. Keep the product in a cool, dry place, away from hot or heated temperatures.</p>
    </div>
    <div class="front">
      <p class="brand">Sugar Lane</p>
      <p class="product-kicker">Calm Dune</p>
      <p class="product-main">Hush</p>
      <p class="product-type">Whipped Body Sugar Scrub</p>
      <p class="size">8oz</p>
    </div>
    <div class="column column--right">
      <p><strong>Directions:</strong> Apply to wet skin gently in a circular motion on desired body area, hands, feet, legs, arms, etc. Once you have a good scrub, rinse, pat dry, and enjoy soft, hydrated skin. Best to use in the shower. Use between 2-3 times a week if needed.</p>
      <p><strong>Cautions:</strong> (1) Allergy: Approach this product with extreme caution, if you have allergies (2) Avoid direct contact with eyes</p>
      <div class="claims">All Natural, Cruelty-Free, Vegan Free<br>No Mineral Oil | No Petroleum | No Parabens</div>
    </div>
  </section>

</main>
</body>
</html>
```